Harborlight Vitality Studio Business Cards and Stationary
Harborlight Vitality Studio
Harborlight Vitality Studio Business Cards and Stationary - Massage Therapy
Creative Brief
Use same font as used in my logo
Similar font as in the word Foundation, or whatever you feel is appropriate
Professional
Dr. Raymond Okafor, D.C.
Every Step Starts With Balance
none at the moment
877 Go Align (462-5446)
www.frontdesk@harborlightvitalitystudio.com
www.harborlightvitalitystudio.com
1.I would like my Logo on top 2. Every Step Starts With Balance 3. Dr. Raymond Okafor, D.C. 4. 877 Go Align (462-5446) 5.email the web site

```html
<!DOCTYPE html>
<html lang="en">
<head>
<meta charset="UTF-8">
<title>Harborlight Vitality Studio Business Cards</title>
<link rel="stylesheet" href="https://fonts.googleapis.com/css2?family=Raleway:ital,wght@0,400;0,600;0,700;1,400;1,600&display=swap">
<style>
  :root {
    --page-bg: #e9ebee;
    --card-bg: #ffffff;
    --brand-blue: #1d6fb3;
    --brand-blue-dark: #14508a;
    --brand-red: #c8232c;
    --brand-teal: #2a9bb7;
    --text-grey: #5a5f66;
    --icon-orange: #e2672a;
    --card-shadow: 0 18px 40px rgba(30, 40, 60, 0.18);
  }
  * { box-sizing: border-box; margin: 0; padding: 0; }
  html, body {
    width: 1200px;
    height: 1009px;
    overflow: hidden;
    background: var(--page-bg);
    font-family: "Raleway", Arial, sans-serif;
  }
  .sheet {
    position: relative;
    width: 1200px;
    height: 1009px;
  }
  .card {
    position: absolute;
    left: 250px;
    width: 700px;
    height: 400px;
    background: var(--card-bg);
    border-radius: 26px;
    box-shadow: var(--card-shadow);
    overflow: hidden;
  }
  .card--front { top: 70px; }
  .card--back { top: 540px; }

  .card__accent {
    position: absolute;
    left: 0;
    right: 0;
    bottom: 0;
    height: 90px;
    background: linear-gradient(180deg, rgba(200, 35, 44, 0.85) 0%, var(--brand-blue) 55%, var(--brand-blue-dark) 100%);
  }

  .brand {
    position: absolute;
    display: flex;
    align-items: center;
    gap: 14px;
  }
  .brand__dot {
    width: 44px;
    height: 44px;
    border-radius: 50%;
    background: var(--brand-teal);
    flex: none;
  }
  .brand__name {
    font-weight: 700;
    color: var(--brand-blue);
    font-size: 30px;
    letter-spacing: 0.5px;
    white-space: nowrap;
  }
  .card--front .brand { left: 44px; top: 46px; }

  .details {
    position: absolute;
    right: 46px;
    top: 128px;
    text-align: right;
  }
  .details__person {
    font-weight: 700;
    color: var(--brand-red);
    font-size: 19px;
  }
  .details__tagline {
    font-style: italic;
    color: var(--brand-blue);
    font-size: 16px;
    margin-top: 4px;
  }
  .contact-list {
    list-style: none;
    margin-top: 18px;
  }
  .contact-list__item {
    display: flex;
    justify-content: flex-end;
    align-items: center;
    gap: 8px;
    font-size: 13px;
    color: var(--text-grey);
    line-height: 22px;
  }
  .contact-list__icon {
    width: 16px;
    height: 16px;
    flex: none;
  }

  .card--back .brand {
    left: 0;
    right: 0;
    top: 150px;
    justify-content: center;
  }
  .card--back .brand__dot { width: 56px; height: 56px; }
  .card--back .brand__name { font-size: 32px; }
  .back__url {
    position: absolute;
    left: 0;
    right: 0;
    top: 300px;
    text-align: center;
    font-size: 14px;
    letter-spacing: 4px;
    color: var(--text-grey);
  }
</style>
</head>
<body>
<main class="sheet">

  <section class="card card--front" aria-label="Business card front">
    <div class="card__accent" role="img" aria-label="Decorative red and blue band along the bottom edge"></div>

    <div class="brand">
      <span class="brand__dot"></span>
      <span class="brand__name">Harborlight Vitality Studio</span>
    </div>

    <div class="details">
      <p class="details__person">Dr. Raymond Okafor, D.C.</p>
      <p class="details__tagline">Every Step Starts With Balance</p>
      <ul class="contact-list">
        <li class="contact-list__item">
          <svg class="contact-list__icon" viewBox="0 0 16 16" aria-hidden="true"><circle cx="8" cy="8" r="8" fill="var(--icon-orange)"/><path d="M5.5 4.5c.4-.3.9-.2 1.1.2l.6 1.2c.2.4 0 .7-.3 1l-.4.3c.4.9 1.1 1.6 2 2l.3-.4c.3-.3.6-.5 1-.3l1.2.6c.4.2.5.7.2 1.1-.6.8-1.4 1-2.3.6A7 7 0 0 1 4.9 6.8c-.4-.9-.2-1.7.6-2.3z" fill="#fff"/></svg>
          <span>877 Go Align (462-5446)</span>
        </li>
        <li class="contact-list__item">
          <svg class="contact-list__icon" viewBox="0 0 16 16" aria-hidden="true"><circle cx="8" cy="8" r="8" fill="var(--icon-orange)"/><rect x="4" y="5" width="8" height="6" rx="1" fill="#fff"/><path d="M4.3 5.4 8 8.3l3.7-2.9" fill="none" stroke="var(--icon-orange)" stroke-width="1"/></svg>
          <span>www.frontdesk@harborlightvitalitystudio.com</span>
        </li>
        <li class="contact-list__item">
          <svg class="contact-list__icon" viewBox="0 0 16 16" aria-hidden="true"><circle cx="8" cy="8" r="8" fill="var(--icon-orange)"/><circle cx="8" cy="8" r="4" fill="none" stroke="#fff" stroke-width="1.1"/><path d="M4 8h8M8 4c-1.6 2.2-1.6 5.8 0 8M8 4c1.6 2.2 1.6 5.8 0 8" fill="none" stroke="#fff" stroke-width="0.9"/></svg>
          <span>www.harborlightvitalitystudio.com</span>
        </li>
      </ul>
    </div>
  </section>

  <section class="card card--back" aria-label="Business card back">
    <div class="brand">
      <span class="brand__dot"></span>
      <span class="brand__name">Harborlight Vitality Studio</span>
    </div>
    <p class="back__url">www.harborlightvitalitystudio.com</p>
  </section>

</main>
</body>
</html>
```